Coffeeshop menu for filter tip

We want to have a cannabis (coffeeshop) menu in the size 25mm wide x 60mm wide. Some examples attached.

it must have the following text:
Menu

WEED p/g
Velotrine €16
Cinderfox €14
Tide Rambler €14
Marigolden €16
Grand Pelican €14
Copper Comet €14

HASH p/g
Baltic Ember €12
Harbor Velvet€11
Plum Rova €14
Dusk Maple €10

Target Market(s)

tourist in Amsterdam

Requirements
Nice to have
• cannabis sign leaf
• No Cigarettes allowed symbol

```html
<!DOCTYPE html>
<html lang="en">
<head>
<meta charset="utf-8">
<title>Amsterdam Menu</title>
<link href="https://fonts.googleapis.com/css2?family=Roboto+Slab:wght@300;400;700&family=Roboto:wght@300;400&display=swap" rel="stylesheet">
<style>
  :root {
    --green: #5cb848;
    --green-dark: #3e8a30;
    --cream: #f3f1cd;
    --white: #ffffff;
    --ink: #2f2f2f;
    --rule-grey: #a9a89a;
    --rule-green: #8fd07e;
    --leaf-tint: rgba(150, 190, 120, 0.28);
    --no-red: #e23b2e;
  }
  * { margin: 0; padding: 0; box-sizing: border-box; }
  html, body { width: 1200px; height: 2873px; overflow: hidden; background: var(--white); }
  .menu-card { position: relative; width: 1200px; height: 2873px; background: var(--white); overflow: hidden; }

  .card-panel { position: absolute; left: 41px; top: 484px; width: 1098px; height: 2389px; background: var(--cream); }

  .header-band { position: absolute; left: 0; top: 0; width: 1200px; height: 484px; background: var(--green); }
  .header-title { position: absolute; left: 122px; top: 112px; width: 660px; color: var(--white); font-family: "Roboto Slab", serif; font-weight: 700; line-height: 1; white-space: nowrap; }
  .header-title .city { display: block; font-size: 100px; letter-spacing: 0; }
  .header-title .word { display: block; font-size: 200px; margin-top: 6px; letter-spacing: 2px; }
  .header-emblem { position: absolute; left: 818px; top: 142px; width: 244px; height: 244px; border-radius: 50%; border: 9px solid var(--white); }
  .header-emblem .emblem-fill { position: absolute; inset: 28px; border-radius: 50%; background: radial-gradient(circle, rgba(255,255,255,0.95) 0%, rgba(255,255,255,0.75) 55%, rgba(255,255,255,0) 75%); }

  .leaf-backdrop { position: absolute; left: 500px; top: 760px; width: 700px; height: 1680px; background: radial-gradient(ellipse at 50% 45%, var(--leaf-tint) 0%, rgba(150,190,120,0.12) 45%, rgba(150,190,120,0) 70%); }

  .section-ribbon { position: absolute; left: 0; width: 665px; height: 237px; }
  .section-ribbon svg { position: absolute; left: 0; top: 0; }
  .section-ribbon .ribbon-label { position: absolute; left: 146px; top: 68px; color: var(--white); font-family: "Roboto Slab", serif; font-weight: 700; font-size: 96px; line-height: 1; letter-spacing: 1px; }

  .unit-label { position: absolute; left: 886px; font-family: "Roboto", sans-serif; font-weight: 300; font-size: 62px; color: var(--ink); }

  .price-list { position: absolute; left: 0; width: 1200px; list-style: none; }
  .price-row { position: relative; height: 118px; }
  .item-name, .item-price { position: absolute; top: 18px; font-family: "Roboto Slab", serif; font-weight: 300; font-size: 70px; line-height: 1; color: var(--ink); white-space: nowrap; }
  .item-name { left: 145px; }
  .item-price { left: 889px; }
  .price-row::before { content: ""; position: absolute; left: 145px; width: 521px; bottom: 0; height: 3px; background: var(--rule-grey); }
  .price-row::after { content: ""; position: absolute; left: 818px; width: 257px; bottom: 0; height: 3px; background: var(--rule-green); }

  .notice { position: absolute; left: 190px; top: 2624px; display: flex; align-items: center; gap: 86px; }
  .notice-text { font-family: "Roboto", sans-serif; font-weight: 400; font-size: 78px; color: var(--ink); }
</style>
</head>
<body>
<div class="menu-card">
  <div class="card-panel"></div>

  <header class="header-band">
    <h1 class="header-title"><span class="city">AMSTERDAM</span><span class="word">MENU</span></h1>
    <div class="header-emblem"><div class="emblem-fill" role="img" aria-label="Cannabis leaf emblem"></div></div>
  </header>

  <div class="leaf-backdrop" role="img" aria-label="Faint large cannabis leaf in the background"></div>

  <section class="menu-section weed-section">
    <div class="section-ribbon" style="top:608px;">
      <svg width="665" height="280" viewBox="0 0 665 280">
        <polygon points="0,0 600,0 665,118 600,237 0,237" fill="var(--green)"/>
        <polygon points="0,237 41,237 41,278" fill="var(--green-dark)"/>
      </svg>
      <span class="ribbon-label">WEED</span>
    </div>
    <span class="unit-label" style="top:780px;">p/g</span>
    <ul class="price-list" style="top:902px;">
      <li class="price-row"><span class="item-name">Velotrine</span><span class="item-price">€16</span></li>
      <li class="price-row"><span class="item-name">Cinderfox</span><span class="item-price">€14</span></li>
      <li class="price-row"><span class="item-name">Tide Rambler</span><span class="item-price">€14</span></li>
      <li class="price-row"><span class="item-name">Marigolden</span><span class="item-price">€16</span></li>
      <li class="price-row"><span class="item-name">Grand Pelican</span><span class="item-price">€14</span></li>
      <li class="price-row"><span class="item-name">Copper Comet</span><span class="item-price">€14</span></li>
    </ul>
  </section>

  <section class="menu-section hash-section">
    <div class="section-ribbon" style="top:1757px;">
      <svg width="665" height="280" viewBox="0 0 665 280">
        <polygon points="0,0 600,0 665,118 600,237 0,237" fill="var(--green)"/>
        <polygon points="0,237 41,237 41,278" fill="var(--green-dark)"/>
      </svg>
      <span class="ribbon-label">HASH</span>
    </div>
    <span class="unit-label" style="top:1898px;">p/g</span>
    <ul class="price-list" style="top:2050px;">
      <li class="price-row"><span class="item-name">Baltic Ember</span><span class="item-price">€12</span></li>
      <li class="price-row"><span class="item-name">Harbor Velvet</span><span class="item-price">€11</span></li>
      <li class="price-row"><span class="item-name">Plum Rova</span><span class="item-price">€14</span></li>
      <li class="price-row"><span class="item-name">Dusk Maple</span><span class="item-price">€10</span></li>
    </ul>
  </section>

  <div class="notice">
    <svg width="160" height="160" viewBox="0 0 160 160" aria-hidden="true">
      <circle cx="80" cy="80" r="70" fill="var(--white)" stroke="var(--no-red)" stroke-width="13"/>
      <g transform="rotate(-35 80 80)">
        <rect x="26" y="70" width="82" height="20" fill="#f2f2f2" stroke="#999" stroke-width="2"/>
        <rect x="108" y="70" width="26" height="20" fill="#e59a3c"/>
      </g>
      <line x1="32" y1="32" x2="128" y2="128" stroke="var(--no-red)" stroke-width="13"/>
    </svg>
    <span class="notice-text">No Cigarette</span>
  </div>
</div>
</body>
</html>
```